I Need a Banner for Web Advertising

impression banner for zentora AD
size 728x90, 320x50 , 160x600 , 300x600 , 100x50
Banner background bright blue
would like the AD to say -
We pay cash for houses in any condition
Probate,foreclosure, Pass due property taxes ect
470-555-0193
Updates
We would like to change the words to -
We pay cash for houses in any condition!
Probate, Foreclosure, Pass Due Property Taxes, and more!
470-555-0193
Target Market(s)
consumers that need to sale
Industry/Entity Type
Real Estate

```html
<!DOCTYPE html>
<html lang="en">
<head>
<meta charset="utf-8">
<title>Zentora – Web Banner Set</title>
<link rel="stylesheet" href="https://fonts.googleapis.com/css2?family=Barlow:ital,wght@0,400;0,500;0,700;0,800;1,700;1,800&display=swap">
<style>
  :root {
    --page: #474747;
    --paper: #f0f4f6;
    --white: #ffffff;
    --ink: #141414;
    --orange: #f7941d;
    --photo-sky: #b9b7ad;
    --photo-wall: #8e8a7f;
    --photo-green: #6c7650;
    --photo-ground: #4f5a35;
  }
  * { box-sizing: border-box; margin: 0; padding: 0; }
  html, body { width: 1200px; height: 900px; overflow: hidden; }
  body {
    background: var(--page);
    font-family: "Barlow", Arial, sans-serif;
    color: var(--ink);
    position: relative;
  }
  .banner { position: absolute; overflow: hidden; background: var(--paper); }
  .abs { position: absolute; white-space: nowrap; }
  .brand { font-weight: 800; color: var(--ink); letter-spacing: 0.02em; line-height: 1; }
  .headline { font-weight: 500; line-height: 1; }
  .condition { font-weight: 800; font-style: italic; color: var(--orange); line-height: 1; }
  .details { font-weight: 500; line-height: 1.3; }
  .cta { font-weight: 800; line-height: 1; }
  .phone-box {
    position: absolute; background: var(--white); border-radius: 8px;
    display: flex; align-items: center; justify-content: center;
    font-weight: 500; box-shadow: 0 2px 3px rgba(0,0,0,0.25);
  }
  .url { font-weight: 500; color: var(--ink); line-height: 1; }
  .photo {
    position: absolute;
    background: linear-gradient(180deg, var(--photo-sky) 0%, var(--photo-wall) 40%, var(--photo-green) 72%, var(--photo-ground) 100%);
  }
  .orange-panel { position: absolute; background: var(--orange); }
  .center { text-align: center; }
  ul.bullets { list-style: none; }
  ul.bullets li { position: relative; }
  ul.bullets li::before {
    content: ""; position: absolute; left: -1.1em; top: 0.45em;
    width: 0.45em; height: 0.45em; border-radius: 50%; background: var(--ink);
  }

  /* Large billboard */
  .billboard { left: 159px; top: 31px; width: 873px; height: 457px; }
  .billboard .photo { left: 432px; top: 0; width: 441px; height: 457px; }
  .billboard .photo-fade {
    position: absolute; left: 432px; top: 0; width: 200px; height: 457px;
    background: linear-gradient(90deg, var(--paper) 0%, rgba(240,244,246,0) 100%);
  }

  /* Leaderboard 728x90 */
  .leaderboard { left: 159px; top: 518px; width: 548px; height: 68px; }
  .leaderboard .photo { left: 230px; top: 0; width: 192px; height: 68px; }
  .leaderboard .photo-fade {
    position: absolute; left: 230px; top: 0; width: 70px; height: 68px;
    background: linear-gradient(90deg, var(--paper), rgba(240,244,246,0));
  }

  /* Mobile 320x50 */
  .mobile { left: 159px; top: 616px; width: 273px; height: 42px; }
  .mobile .photo { left: 118px; top: 0; width: 96px; height: 42px; }
  .mobile .photo-fade {
    position: absolute; left: 118px; top: 0; width: 36px; height: 42px;
    background: linear-gradient(90deg, var(--paper), rgba(240,244,246,0));
  }

  /* Small 100x50 */
  .tiny { left: 159px; top: 688px; width: 80px; height: 40px; }
  .tiny .photo { left: 34px; top: 0; width: 46px; height: 40px; }

  /* Skyscraper 160x600 */
  .skyscraper { left: 732px; top: 518px; width: 95px; height: 357px; background: var(--orange); }
  .skyscraper .card {
    position: absolute; left: 0; top: 0; width: 95px; height: 297px;
    background: var(--white); border-bottom-right-radius: 8px; overflow: hidden;
  }
  .skyscraper .photo { left: 0; top: 0; width: 95px; height: 128px; }
  .skyscraper .photo-fade {
    position: absolute; left: 0; top: 90px; width: 95px; height: 40px;
    background: linear-gradient(180deg, rgba(255,255,255,0), var(--white));
  }

  /* Half page 300x600 */
  .halfpage { left: 855px; top: 518px; width: 177px; height: 354px; background: var(--orange); }
  .halfpage .card {
    position: absolute; left: 0; top: 0; width: 177px; height: 277px;
    background: var(--white); border-bottom-right-radius: 16px; overflow: hidden;
  }
  .halfpage .photo { left: 0; top: 0; width: 177px; height: 127px; }
  .halfpage .photo-fade {
    position: absolute; left: 0; top: 95px; width: 177px; height: 34px;
    background: linear-gradient(180deg, rgba(255,255,255,0), var(--white));
  }
</style>
</head>
<body>

<!-- Large billboard -->
<section class="banner billboard">
  <div class="photo" role="img" aria-label="Photo of an abandoned boarded-up house covered in graffiti, surrounded by bare trees and overgrown brush"></div>
  <div class="photo-fade"></div>
  <svg class="abs" style="left:0;top:0" width="873" height="457" viewBox="0 0 873 457">
    <polygon points="546,457 873,256 873,457" fill="#f7941d"/>
  </svg>
  <div class="abs brand" style="left:25px;top:40px;font-size:82px;">ZENTORA</div>
  <div class="abs headline" style="left:26px;top:165px;font-size:36px;letter-spacing:0.02em;">WE PAY CASH FOR HOUSES</div>
  <div class="abs condition" style="left:26px;top:212px;font-size:66px;letter-spacing:0.01em;">ANY CONDITION</div>
  <div class="abs details" style="left:29px;top:292px;font-size:25px;line-height:1.35;letter-spacing:0.02em;">Probate, Foreclosure, Past due<br>property taxes ect.......</div>
  <div class="abs url" style="left:26px;top:401px;font-size:25px;letter-spacing:0.03em;">www.zentorahomes.com</div>
  <div class="abs cta" style="left:697px;top:357px;font-size:30px;">CALL NOW!!</div>
  <div class="phone-box" style="left:688px;top:391px;width:176px;height:49px;font-size:24px;">470-555-0193</div>
</section>

<!-- Leaderboard 728x90 -->
<section class="banner leaderboard">
  <div class="photo" role="img" aria-label="Photo of an abandoned graffiti-covered house"></div>
  <div class="photo-fade"></div>
  <div class="orange-panel" style="left:421px;top:0;width:127px;height:68px;"></div>
  <div class="abs headline" style="left:31px;top:9px;font-size:14px;">WE PAY CASH FOR HOUSES</div>
  <div class="abs condition" style="left:23px;top:24px;font-size:27px;">ANY CONDITION</div>
  <div class="abs details" style="left:23px;top:53px;font-size:8px;">Probate, Foreclosure, Past due property taxes ect.......</div>
  <div class="abs brand" style="left:258px;top:11px;font-size:15px;">ZENTORA</div>
  <div class="abs cta center" style="left:421px;top:7px;width:127px;font-size:14px;">CALL NOW!!</div>
  <div class="phone-box" style="left:440px;top:27px;width:90px;height:22px;font-size:11px;border-radius:6px;">470-555-0193</div>
  <div class="abs url center" style="left:421px;top:54px;width:127px;font-size:7.5px;">www.zentorahomes.com</div>
</section>

<!-- Mobile 320x50 -->
<section class="banner mobile">
  <div class="photo" role="img" aria-label="Photo of an abandoned graffiti-covered house"></div>
  <div class="photo-fade"></div>
  <div class="orange-panel" style="left:213px;top:0;width:60px;height:42px;"></div>
  <div class="abs headline" style="left:10px;top:6px;font-size:7.5px;">WE PAY CASH FOR HOUSES</div>
  <div class="abs condition" style="left:6px;top:14px;font-size:14px;">ANY CONDITION</div>
  <div class="abs details" style="left:7px;top:31px;font-size:4.5px;">Probate, Foreclosure, Past due property taxes and more</div>
  <div class="abs brand" style="left:126px;top:7px;font-size:9px;">ZENTORA</div>
  <div class="abs cta center" style="left:213px;top:5px;width:60px;font-size:7.5px;">CALL NOW!!</div>
  <div class="phone-box" style="left:217px;top:16px;width:52px;height:13px;font-size:6.5px;border-radius:4px;">470-555-0193</div>
  <div class="abs url center" style="left:213px;top:33px;width:60px;font-size:4px;">www.zentorahomes.com</div>
</section>

<!-- Small 100x50 -->
<section class="banner tiny">
  <div class="photo" role="img" aria-label="Photo of an abandoned house"></div>
  <svg class="abs" style="left:0;top:0" width="80" height="40" viewBox="0 0 80 40">
    <polygon points="52,40 80,24 80,40" fill="#f7941d"/>
  </svg>
  <div class="abs brand" style="left:3px;top:4px;font-size:6.5px;">ZENTORA</div>
  <div class="abs headline" style="left:5px;top:14px;font-size:3px;">WE PAY CASH FOR HOUSES</div>
  <div class="abs condition" style="left:3px;top:18px;font-size:6.5px;">ANY CONDITION</div>
  <div class="abs details" style="left:3px;top:26px;font-size:2.6px;">Probate, foreclosure, taxes and more</div>
  <div class="abs url" style="left:3px;top:34px;font-size:2.4px;">www.zentorahomes.com</div>
  <div class="abs cta" style="left:60px;top:28px;font-size:3px;">CALL NOW!!</div>
  <div class="phone-box" style="left:57px;top:33px;width:20px;height:5px;font-size:2.4px;border-radius:2px;">470-555-0193</div>
</section>

<!-- Skyscraper 160x600 -->
<section class="banner skyscraper">
  <div class="card">
    <div class="photo" role="img" aria-label="Photo of an abandoned graffiti-covered house with overgrown yard"></div>
    <div class="photo-fade"></div>
    <div class="abs brand center" style="left:0;top:15px;width:95px;font-size:12px;">ZENTORA</div>
    <div class="abs headline center" style="left:0;top:137px;width:95px;font-size:13px;line-height:1.2;">WE PAY<br>CASH FOR<br>HOUSES</div>
    <div class="abs condition center" style="left:0;top:190px;width:95px;font-size:14px;line-height:1;">ANY<br>CONDITION</div>
    <ul class="abs bullets details" style="left:13px;top:230px;font-size:7.5px;line-height:1.85;">
      <li>Probate,</li>
      <li>Foreclosure,</li>
      <li>Past due property<br>taxes ect...</li>
    </ul>
  </div>
  <div class="abs headline center" style="left:0;top:307px;width:95px;font-size:12.5px;font-weight:500;">CALL NOW!!</div>
  <div class="phone-box" style="left:7px;top:320px;width:81px;height:19px;font-size:10px;border-radius:6px;">470-555-0193</div>
  <div class="abs url center" style="left:0;top:345px;width:95px;font-size:6px;">www.zentorahomes.com</div>
</section>

<!-- Half page 300x600 -->
<section class="banner halfpage">
  <div class="card">
    <div class="photo" role="img" aria-label="Photo of an abandoned graffiti-covered house with overgrown yard"></div>
    <div class="photo-fade"></div>
    <div class="abs brand center" style="left:0;top:15px;width:177px;font-size:20px;">ZENTORA</div>
    <div class="abs headline center" style="left:0;top:126px;width:177px;font-size:21px;line-height:1.2;">WE PAY CASH<br>FOR HOUSES</div>
    <div class="abs condition center" style="left:0;top:179px;width:177px;font-size:18.5px;">ANY CONDITION</div>
    <ul class="abs bullets details" style="left:28px;top:205px;font-size:10.5px;line-height:1.6;letter-spacing:0.02em;">
      <li>Probate,</li>
      <li>Foreclosure,</li>
      <li>Past due property taxes<br>ect...</li>
    </ul>
  </div>
  <div class="abs headline center" style="left:0;top:285px;width:177px;font-size:20px;">CALL NOW!!</div>
  <div class="phone-box" style="left:32px;top:307px;width:117px;height:28px;font-size:15px;">470-555-0193</div>
  <div class="abs url center" style="left:0;top:340px;width:177px;font-size:9.5px;">www.zentorahomes.com</div>
</section>

</body>
</html>
```